Help our Crumb Parlour find our winning design! We're looking for a business card....

We’re a Crumb Parlour in NY specializing in custom-made cakes and unique desserts.
Our cakes combine flavor and art, each designed to match customer’s special event and theme.
We’d like a unique business card with a clean design that will combine French chic and artistic look & feel.
We’d like to differentiate ourselves from standard bakeries, please don’t offer cupcake images :-)
Our logo is peach-pink and brown and we’d love to use these colors ( . Another color that can be added is gold - or feel free to suggest!

Target Market(s)

Women, ages 25-55

Industry/Entity Type

Boutique

Contact Information for Business Card

Text on card:
Logo
Crumb Parlour by Dana Whitfield

www.xxxxxxxx.com
xxx@xxxxx.com
(516) xxx-xxxx
F – xxxxxxxxxx
IG - xxxxxxxxx

Font styles to use
Sans Serif
Script

Requirements
Must have
• Logo
• Clean look
• French chic and artistic look & feel.
Nice to have
• Damask pattern
Should not have
• Cupcake images

```html
<!DOCTYPE html>
<html lang="en">
<head>
<meta charset="utf-8">
<title>Crumb Parlour – Business Card</title>
<link rel="stylesheet" href="https://fonts.googleapis.com/css2?family=Montserrat:wght@300;400;600&display=swap">
<style>
  :root {
    --backdrop: #d9cdb6;
    --card-light: #f4f4f4;
    --card-shade: #d6d6d6;
    --cocoa: #4b4545;
    --ink: #221f1f;
    --blush: #f4a2b4;
    --blush-deep: #e48aa0;
    --white: #ffffff;
    --social: #3a8fd8;
  }
  html, body {
    margin: 0;
    width: 1057px;
    height: 1200px;
    overflow: hidden;
    background: var(--backdrop);
    font-family: "Montserrat", sans-serif;
  }
  .sheet {
    position: relative;
    width: 1057px;
    height: 1200px;
  }
  .card {
    position: absolute;
    left: 78px;
    width: 900px;
    height: 514px;
    box-shadow: 0 14px 30px rgba(60, 45, 25, 0.35);
  }
  .card--front { top: 60px; }
  .card--back  { top: 626px; }
  .card svg { display: block; }
  .brand-name {
    font-family: "Montserrat", sans-serif;
    font-weight: 300;
    letter-spacing: 6px;
    fill: var(--ink);
  }
  .person-name {
    font-weight: 600;
    letter-spacing: 5px;
    fill: var(--white);
  }
  .person-role {
    font-weight: 400;
    letter-spacing: 4px;
    fill: var(--white);
  }
  .contact {
    font-weight: 400;
    letter-spacing: 1px;
    fill: var(--white);
  }
</style>
</head>
<body>
<main class="sheet">

  <section class="card card--front" aria-label="Card front">
    <svg width="900" height="514" viewBox="0 0 900 514">
      <defs>
        <radialGradient id="paperFront" cx="50%" cy="45%" r="70%">
          <stop offset="0" stop-color="var(--card-light)"/>
          <stop offset="1" stop-color="var(--card-shade)"/>
        </radialGradient>
      </defs>
      <rect class="frame-outer" width="900" height="514" fill="var(--ink)"/>
      <rect class="frame-blush" x="18" y="18" width="864" height="478" fill="var(--blush)"/>
      <rect class="paper" x="34" y="34" width="832" height="446" fill="url(#paperFront)"/>
      <circle class="brand-dot" cx="281" cy="257" r="9" fill="var(--blush)"/>
      <text class="brand-name" x="304" y="268" font-size="34">Crumb Parlour</text>
    </svg>
  </section>

  <section class="card card--back" aria-label="Card back">
    <svg width="900" height="514" viewBox="0 0 900 514">
      <defs>
        <linearGradient id="paperBack" x1="0" y1="0" x2="1" y2="1">
          <stop offset="0" stop-color="var(--card-light)"/>
          <stop offset="1" stop-color="var(--card-shade)"/>
        </linearGradient>
      </defs>
      <rect class="paper" width="900" height="514" fill="url(#paperBack)"/>

      <polygon class="band-blush-diag" points="560,0 640,0 470,300 390,300" fill="var(--blush)"/>
      <polygon class="band-cocoa" points="648,0 900,0 900,514 0,514 0,320 466,320 640,14" fill="var(--cocoa)"/>
      <rect class="band-rule" x="0" y="470" width="900" height="10" fill="var(--card-shade)" opacity="0.5"/>

      <circle class="brand-dot" cx="96" cy="150" r="8" fill="var(--blush)"/>
      <text class="brand-name" x="116" y="160" font-size="28">Crumb Parlour</text>

      <g class="phone-lines">
        <rect x="680" y="20" width="16" height="16" fill="var(--blush-deep)"/>
        <path d="M684 24 l3 0 l1 3 l-2 1 q1 3 4 4 l1 -2 l3 1 l0 3 q-9 0 -10 -10z" fill="var(--white)"/>
        <text class="contact" x="706" y="33" font-size="15">(516) 555-0142</text>
        <rect x="680" y="44" width="16" height="16" fill="var(--blush-deep)"/>
        <path d="M684 48 l3 0 l1 3 l-2 1 q1 3 4 4 l1 -2 l3 1 l0 3 q-9 0 -10 -10z" fill="var(--white)"/>
        <text class="contact" x="706" y="57" font-size="15">(516) 555-0187</text>
      </g>

      <text class="person-name" x="40" y="372" font-size="30">DANA WHITFIELD</text>
      <text class="person-role" x="40" y="402" font-size="16">FOUNDER</text>

      <rect class="address-marker" x="40" y="424" width="14" height="14" fill="var(--social)"/>
      <text class="contact" x="64" y="436" font-size="14">214 Bleecker Street, New York, NY</text>
      <text class="contact" x="520" y="400" font-size="14">www.crumbparlour.com</text>
      <text class="contact" x="520" y="424" font-size="14">hello@crumbparlour.com</text>
    </svg>
  </section>

</main>
</body>
</html>
```